Company corporate advertising sign and banner for different uses

Hello,
We are a handcraft business and in need of an advertising sign and banner for different uses based on our company logo.
The banner should be usable mainly for advertising on different websites and as this we think it should be in landscape format.
The advertising sign should be usable in different sizes. Firstly we would need it in 50cmx60cm or similar format, so we can let it print on plexiglas or as a plastic sign (and similar) to screw it on a wall near our company so people (mainly delivery companies) are able to find our warehouse on the other side we would need this same sign in plastic or perhaps thin metal to put it as an advertising and contact sign on our different projects that we are realizing, for example car barriers, video surveillance systems, alarm systems for home or company use (outside on the sirenes), on electric boxes like car charging stations, computers and much other things, so you see the very need that we must be able to change the size of the advertising sign but it must still be recognizable that our company realized that sort of work.
We have a logo that must be represented on that sign and also our company details must be present, so people are able to contact us.
The advertising sign and the banner should go hand in hand, so that everyone can recognize on first sight that it is our company.
We put our logo in the upload files section, the text on the right side of the logo can be used but is not an absolute must, depends on the ideas of the design and the designer.
The text we absolutely would need is beside our phone, website address and email address which are :
+352 27419586
www.plostermaak.lu
info@plostermaak.lu
the following text, representing our services :
Réparations et rénovations tout genre
Electricité générale, dépannages, domotique, systèmes d'alarme et de vidéosurveillance
Solutions et services en informatique
Aménagements de l'extérieur, services de jardinage
Thanks very much
Target Market(s)
private and business customers
Industry/Entity Type
craft business

```html
<!DOCTYPE html>
<html lang="fr">
<head>
<meta charset="utf-8">
<title>de Plostermaak – panneau publicitaire</title>
<link rel="stylesheet" href="https://fonts.googleapis.com/css2?family=Bebas+Neue&family=Eczar:wght@400;600;700&family=Poppins:wght@300&display=swap">
<style>
  :root {
    --ink: #231838;
    --orange: #f7ae47;
    --white: #ffffff;
    --backdrop: #e8e8e8;
  }
  * { box-sizing: border-box; margin: 0; padding: 0; }
  html, body { width: 1200px; height: 1024px; overflow: hidden; background: var(--backdrop); }
  .sign {
    position: absolute; left: 200px; top: 31px;
    width: 800px; height: 961px;
    background: var(--white);
    overflow: hidden;
    font-family: "Eczar", Georgia, serif;
    color: var(--ink);
  }
  .sign__top-rule { position: absolute; left: 0; top: 0; width: 800px; height: 11px; background: var(--ink); }
  .header { position: absolute; left: 0; top: 11px; width: 800px; height: 294px; }
  .header__shapes { position: absolute; left: 0; top: -11px; }
  .brand-mark {
    position: absolute; left: 172px; top: 70px; width: 140px; height: 140px;
    background: var(--ink);
  }
  .brand-name {
    position: absolute; left: 372px; top: 86px;
    font-family: "Eczar", Georgia, serif; font-weight: 700;
    font-size: 40px; line-height: 1; color: var(--ink); white-space: nowrap;
  }
  .brand-tagline {
    position: absolute; left: 420px; top: 136px;
    font-family: "Poppins", Arial, sans-serif; font-weight: 300;
    font-size: 21px; color: var(--ink); white-space: nowrap;
  }
  .phone {
    position: absolute; left: 356px; top: 190px; height: 62px;
    display: flex; align-items: center; gap: 8px;
    color: var(--orange);
  }
  .phone__icon { width: 36px; height: 36px; }
  .phone__number {
    font-family: "Bebas Neue", Impact, sans-serif;
    font-size: 62px; line-height: 1; letter-spacing: 0.5px; padding-top: 6px;
  }
  .services { list-style: none; }
  .service {
    position: absolute; left: 30px; width: 760px;
    display: flex; align-items: flex-start; gap: 16px;
  }
  .service__dot {
    flex: none; width: 36px; height: 36px; margin-top: 2px;
    border: 2px solid var(--ink); border-radius: 50%;
    display: flex; align-items: center; justify-content: center;
  }
  .service__dot::after { content: ""; width: 24px; height: 24px; border-radius: 50%; background: var(--orange); }
  .service__text { font-weight: 600; font-size: 39px; line-height: 37px; letter-spacing: -0.3px; white-space: nowrap; }
  .service--repairs { top: 394px; }
  .service--electric { top: 476px; }
  .service--it { top: 622px; }
  .service--outdoor { top: 702px; }
  .footer {
    position: absolute; left: 0; top: 846px; width: 800px; height: 87px;
    background: var(--ink); color: var(--orange);
    font-family: "Eczar", Georgia, serif; font-weight: 400; font-size: 32px;
  }
  .contact { position: absolute; top: 0; height: 87px; display: flex; align-items: center; gap: 12px; }
  .contact--web { left: 36px; }
  .contact--mail { left: 428px; }
  .contact__icon { width: 32px; height: 32px; }
</style>
</head>
<body>
<main class="sign">
  <div class="sign__top-rule"></div>

  <header class="header">
    <svg class="header__shapes" width="800" height="305" viewBox="0 0 800 305" aria-hidden="true">
      <rect x="0" y="11" width="800" height="294" fill="var(--orange)"/>
      <path d="M236 11 H800 V276 H238 Q222 276 208 268 L140 228 Q125 219 125 200 V110 Q125 84 148 72 Z" fill="var(--white)"/>
      <path d="M342 186 H800 V257 H286 Q272 257 284 248 L330 192 Q335 186 342 186 Z" fill="var(--ink)"/>
    </svg>
    <div class="brand-mark"></div>
    <div class="brand-name">de Plostermaak</div>
    <div class="brand-tagline">fir all Är Projeten</div>
    <div class="phone">
      <svg class="phone__icon" viewBox="0 0 24 24" aria-hidden="true">
        <path d="M6.6 2.5l3 3.2c.5.5.5 1.3 0 1.8L8.2 9c1.2 2.6 3.2 4.6 5.8 5.8l1.5-1.4c.5-.5 1.3-.5 1.8 0l3.2 3c.5.5.5 1.3 0 1.8l-1.8 1.8c-1 1-2.6 1.2-3.8.5C9.6 18 6 14.4 3.5 9.1c-.7-1.2-.5-2.8.5-3.8l1.8-1.8c.3-.3.6-.5.8-.5z" fill="currentColor"/>
        <path d="M14 3.5a7 7 0 0 1 6.5 6.5M14 7a3.5 3.5 0 0 1 3 3" stroke="currentColor" stroke-width="1.6" fill="none" stroke-linecap="round"/>
      </svg>
      <span class="phone__number">+352 27419586</span>
    </div>
  </header>

  <ul class="services">
    <li class="service service--repairs"><span class="service__dot"></span><span class="service__text">Réparations et rénovations tout genre</span></li>
    <li class="service service--electric"><span class="service__dot"></span><span class="service__text">Electricité générale, dépannges,<br>domotique, systémes d’alarme et de<br>vidéosurveillance</span></li>
    <li class="service service--it"><span class="service__dot"></span><span class="service__text">Solutions et services en informatique</span></li>
    <li class="service service--outdoor"><span class="service__dot"></span><span class="service__text">Aménagements de l’extérieur, services<br>de jardinage</span></li>
  </ul>

  <footer class="footer">
    <div class="contact contact--web">
      <svg class="contact__icon" viewBox="0 0 24 24" aria-hidden="true" fill="none" stroke="currentColor" stroke-width="1.5">
        <circle cx="12" cy="12" r="10"/><ellipse cx="12" cy="12" rx="4.5" ry="10"/>
        <path d="M2 12h20M4 6.5h16M4 17.5h16M12 2v20"/>
      </svg>
      <span>www.plostermaak.lu</span>
    </div>
    <div class="contact contact--mail">
      <svg class="contact__icon" viewBox="0 0 24 24" aria-hidden="true" fill="none" stroke="currentColor" stroke-width="1.6">
        <rect x="1.5" y="4.5" width="21" height="15"/><path d="M1.5 4.5l10.5 9 10.5-9M1.5 19.5l8-7.5M22.5 19.5l-8-7.5"/>
      </svg>
      <span>info@plostermaak.lu</span>
    </div>
  </footer>
</main>
</body>
</html>
```